New shopfront/banner design: size

We're re-doing our shopfront with banners/signs and billboard. We have our existing logo that we're happy with, but would like to change the theme and background coloring etc to a more modern look. I've attached our logo and a draft of the billboard.
Guys the billboard size is 10245mm x 1710mm.Please keep this in mind as you work.I also gave you all a rough indication of what i want in the attachment. billboard with pinqora and zelvo logo including our security license number etc. Added Wednesday, August 30, 2017

```html
<!DOCTYPE html>
<html lang="en">
<head>
<meta charset="utf-8">
<title>Halvern Surveillance Products – Billboard</title>
<link rel="stylesheet" href="https://fonts.googleapis.com/css2?family=Arimo:wght@400;700&display=swap">
<style>
  :root {
    --brand-blue: #2f86f0;
    --band-blue: #2b82ee;
    --ink-dark: #262626;
    --ink-grey: #5a5a5a;
    --paper: #ffffff;
    --frame: #9a9a9a;
    --photo-dark: #050505;
    --photo-light: #8a8a8a;
  }
  * { margin: 0; padding: 0; box-sizing: border-box; }
  html, body { width: 1200px; height: 201px; overflow: hidden; background: var(--paper); }
  .billboard {
    position: relative;
    width: 1200px;
    height: 201px;
    background: var(--paper);
    border: 1px solid var(--frame);
    overflow: hidden;
    font-family: "Arimo", Arial, sans-serif;
  }
  .hero-photo {
    position: absolute;
    left: 0; top: 0;
    width: 297px; height: 201px;
    background: linear-gradient(90deg, var(--photo-dark) 0%, #2c2c2c 45%, var(--photo-light) 100%);
  }
  .brand-mark {
    position: absolute;
    left: 483px; top: 12px;
    width: 80px; height: 80px;
    border-radius: 50%;
    background: var(--ink-dark);
  }
  .brand-name {
    position: absolute;
    left: 360px; top: 104px;
    width: 330px;
    text-align: center;
    font-size: 44px;
    line-height: 46px;
    font-weight: 700;
    letter-spacing: 11px;
    text-indent: 11px;
    color: var(--ink-dark);
    white-space: nowrap;
  }
  .brand-descriptor {
    position: absolute;
    left: 350px; top: 150px;
    width: 350px;
    text-align: center;
    font-size: 18px;
    line-height: 18px;
    letter-spacing: 2.6px;
    text-indent: 2.6px;
    color: var(--brand-blue);
    white-space: nowrap;
  }
  .brand-tagline {
    position: absolute;
    left: 350px; top: 175px;
    width: 350px;
    text-align: center;
    font-size: 14px;
    line-height: 16px;
    letter-spacing: 2px;
    text-indent: 2px;
    color: var(--ink-grey);
    white-space: nowrap;
  }
  .service-band {
    position: absolute;
    left: 739px; top: 67px;
    width: 461px; height: 46px;
  }
  .service-band svg { position: absolute; inset: 0; }
  .service-band p {
    position: absolute;
    left: 62px; top: 0;
    height: 46px;
    line-height: 46px;
    font-size: 16px;
    letter-spacing: 4.4px;
    color: var(--paper);
    white-space: nowrap;
  }
  .social {
    position: absolute;
    top: 124px;
    display: flex;
    align-items: flex-end;
    gap: 4px;
    color: var(--ink-dark);
  }
  .social-dot {
    width: 15px; height: 15px;
    background: var(--band-blue);
  }
  .social-label { display: flex; flex-direction: column; }
  .social-label small { font-size: 7px; line-height: 8px; color: var(--ink-dark); }
  .social-label span { font-size: 15px; line-height: 16px; font-weight: 700; }
  .social--pinqora { left: 895px; }
  .social--zelvo { left: 1009px; top: 132px; }
  .licence {
    position: absolute;
    left: 800px; top: 166px;
    width: 365px;
    text-align: center;
    font-size: 17px;
    line-height: 20px;
    color: var(--brand-blue);
    white-space: nowrap;
  }
</style>
</head>
<body>
  <div class="billboard">
    <div class="hero-photo" role="img" aria-label="Photo of a masked burglar in a black jacket peeking around a wall"></div>

    <div class="brand-mark" aria-hidden="true"></div>
    <div class="brand-name">HALVERN</div>
    <div class="brand-descriptor">SURVEILLANCE PRODUCTS</div>
    <div class="brand-tagline">For all your surveillance needs</div>

    <div class="service-band">
      <svg width="461" height="46" viewBox="0 0 461 46" aria-hidden="true">
        <polygon points="44,0 461,0 461,46 0,46" fill="var(--band-blue)"/>
      </svg>
      <p>ALARMS / CCTV / SPY PRODUCTS</p>
    </div>

    <div class="social social--pinqora">
      <div class="social-dot" aria-hidden="true"></div>
      <div class="social-label">
        <small>find us on</small>
        <span>pinqora</span>
      </div>
    </div>
    <div class="social social--zelvo">
      <div class="social-dot" aria-hidden="true"></div>
      <div class="social-label">
        <span>zelvo</span>
      </div>
    </div>

    <div class="licence">SECURITY AGENTS LICENCE : ISL 48213</div>
  </div>
</body>
</html>
```